4747 5858

Web(re)design of an existing directory search site www.le5858.be (in Dutch www.de4747.be and in English www.3737.be).

This site is a directory site, i.e. a "white pages" site whereby people can search the phone & details of another person based on a combination of name + city (for instance pellow in Brussels); one can also search a company also based on a combination of name + city (for instance Vornak in Brussels); last but not least one can also search the name of the subscriber behind a specific telephone number (also called reverse search).

This site is quite outdated and needs a redesign, see instructions.

We need the output in XD format.

```html
<!DOCTYPE html>
<html lang="en">
<head>
<meta charset="utf-8">
<title>Dialbook Directory</title>
<link rel="stylesheet" href="https://fonts.googleapis.com/css2?family=DM+Serif+Display&family=Work+Sans:wght@400;500;600;700&display=swap">
<style>
:root{
  --navy:#231b6e;
  --coral:#fd5a5f;
  --ad:#9ea5af;
  --hero:#eef0f3;
  --panel:#ffffff;
  --tab:#dcdde8;
  --text:#2a2a3a;
  --muted:#a9acb6;
  --footer:#f0f1f3;
}
*{margin:0;padding:0;box-sizing:border-box}
html,body{width:682px;height:1200px;overflow:hidden;background:#fff}
.page{position:relative;width:1456px;height:2562px;transform:scale(.4684);transform-origin:0 0;font-family:"Work Sans",sans-serif;color:var(--text);background:#fff}
.abs{position:absolute}
.serif{font-family:"DM Serif Display",serif;color:var(--navy);font-weight:400}
.caps{text-transform:uppercase;letter-spacing:1.2px;font-weight:600}

/* header */
.site-header{left:0;top:0;width:1456px;height:80px;background:#fff;border-bottom:1px solid #e4e5ea}
.brand{display:flex;align-items:center;gap:10px}
.brand-dot{width:18px;height:18px;border-radius:50%;background:var(--coral)}
.brand-name{font-family:"Work Sans",sans-serif;font-weight:600;font-size:27px;color:var(--navy);letter-spacing:-.3px}
.main-nav{left:457px;top:30px;display:flex;gap:34px;font-size:15px;font-weight:500;color:var(--navy)}
.lang{left:968px;top:16px;width:105px;height:48px;border:2px solid var(--navy);border-radius:24px;display:flex;align-items:center;justify-content:space-between;padding:0 16px 0 20px;font-size:14px;color:var(--navy);font-weight:600}
.login{left:1082px;top:16px;width:176px;height:48px;border:2px solid var(--coral);border-radius:24px;display:flex;align-items:center;justify-content:center;color:var(--coral);font-size:13px}

/* hero */
.hero{left:0;top:81px;width:1456px;height:730px;background:var(--hero)}
.skyline{left:0;top:490px;width:1456px;height:330px;background:linear-gradient(180deg,#eef0f3 0%,#c9ced6 25%,#d3d7de 60%,#ffffff 100%)}
.hero-title{left:0;top:122px;width:1456px;text-align:center;font-size:40px}
.hero-sub{left:0;top:190px;width:1456px;text-align:center;font-size:13.5px;line-height:23px;color:var(--navy);letter-spacing:1.3px}
.tabs{left:294px;top:286px;display:flex;gap:2px}
.tab{height:46px;padding:0 20px;background:var(--tab);border-radius:8px 8px 0 0;display:flex;align-items:center;font-size:14px;color:var(--navy)}
.tab.active{background:var(--navy);color:#fff;padding:0 29px}
.search-box{left:294px;top:332px;width:867px;height:93px;background:#fff;border-radius:0 6px 6px 6px;box-shadow:0 10px 25px rgba(40,40,80,.12)}
.field{top:28px}
.field .label{font-size:13.5px;color:var(--text);letter-spacing:1.2px}
.field .hint{font-size:13px;color:var(--muted);margin-top:6px}
.sep{top:14px;width:1px;height:65px;background:#e2e3e8}
.btn-search{left:696px;top:23px;width:148px;height:47px;border-radius:24px;background:var(--coral);color:#fff;font-size:12.5px;display:flex;align-items:center;justify-content:center;box-shadow:0 8px 16px rgba(253,90,95,.35)}
.browse{left:294px;top:461px;font-size:12.5px;color:var(--navy)}
.cards{left:294px;top:498px;display:flex;gap:8px}
.card{width:151px;height:129px;background:#fff;border-radius:6px;display:flex;flex-direction:column;align-items:center;justify-content:flex-end;padding-bottom:20px;gap:14px;font-size:13.5px;color:var(--navy)}
.card svg{width:58px;height:58px}
.ad{background:var(--ad);color:#fff;display:flex;align-items:center;justify-content:center;text-align:center;font-size:14px;letter-spacing:1.5px;font-weight:700}
.ad-side{left:1194px;top:120px;width:167px;height:513px;line-height:20px}
.content-panel{left:197px;top:676px;width:1061px;height:560px;background:#fff}
.ad-wide{left:248px;width:958px;height:126px}

/* text blocks */
.block-title{font-size:41px}
.block-body{font-size:14.5px;line-height:21.5px;color:var(--text);letter-spacing:-.2px}
.block-body p+p{margin-top:21px}
.illus{border-radius:40px}

/* app band */
.app-band{left:0;top:1228px;width:1456px;height:449px;background:linear-gradient(100deg,#8e1f47 0%,#6f2a68 45%,#3b1c6f 100%)}
.phone-photo{left:375px;top:40px;width:340px;height:409px;border-radius:40px 40px 0 0;background:linear-gradient(160deg,#1b1338 0%,#3c2a6b 45%,#c89a84 75%,#b57f6a 100%)}
.app-title{left:765px;top:55px;font-size:41px;color:#fff}
.app-body{left:766px;top:126px;width:495px;font-size:14.5px;line-height:21.5px;color:#fff;letter-spacing:-.2px}
.store-btn{top:225px;width:231px;height:68px;border-radius:34px;background:var(--coral);color:#fff;display:flex;align-items:center;gap:14px;padding-left:34px}
.store-btn .small{font-size:13px;font-weight:500}
.store-btn .big{font-size:16px;letter-spacing:1.4px;font-weight:700}

/* footer */
.site-footer{left:0;top:2235px;width:1456px;height:327px;background:var(--footer)}
.foot-about{left:197px;top:135px;width:265px;font-size:13.5px;line-height:21.5px;letter-spacing:-.2px}
.foot-head{font-size:13.5px;color:var(--navy);letter-spacing:1.4px}
.foot-list{list-style:none;font-size:13.5px;margin-top:14px}
.foot-list li{line-height:26.5px}
.contact{display:flex;gap:8px;font-size:13.5px;line-height:20px;margin-top:14px}
.social{display:flex;gap:27px;margin-top:20px}
.social span{width:16px;height:16px;border-radius:50%;border:2px solid var(--coral)}
.foot-rule{left:197px;top:240px;width:1061px;height:1px;background:#d9dbe0}
.copyright{left:0;top:275px;width:1456px;text-align:center;font-size:13px;letter-spacing:1.4px;color:var(--navy)}
.copyright b{color:var(--coral);font-weight:600}
</style>
</head>
<body>
<div class="page">

  <section class="abs hero" aria-label="Search"></section>
  <div class="abs skyline" role="img" aria-label="Soft grey city skyline silhouette"></div>
  <div class="abs content-panel"></div>

  <header class="abs site-header">
    <div class="abs brand" style="left:199px;top:22px"><span class="brand-dot"></span><span class="brand-name">Dialbook</span></div>
    <nav class="abs main-nav"><span>Home</span><span>About</span><span>Advertise</span><span>Categories</span><span>Stories</span><span>Help?</span></nav>
    <div class="abs lang">EN
      <svg width="14" height="9" viewBox="0 0 14 9"><path d="M1 1l6 6 6-6" fill="none" stroke="#231b6e" stroke-width="2"/></svg>
    </div>
    <div class="abs login caps">Login/Register</div>
  </header>

  <h1 class="abs serif hero-title">The One number for all Directory enquiries</h1>
  <p class="abs hero-sub caps">Lorem ipsum dolor sit amet, consectetur adipiscing elit. Nunc nisl<br>nisi, tempus mollis eros ac</p>

  <div class="abs tabs caps">
    <div class="tab active">People</div><div class="tab">Companies</div><div class="tab">Reverse</div><div class="tab">International</div>
  </div>
  <form class="abs search-box">
    <div class="abs field" style="left:31px"><div class="label caps">First name:</div><div class="hint">Eg: Dupont, Janssen, ...</div></div>
    <div class="abs sep" style="left:197px"></div>
    <div class="abs field" style="left:236px"><div class="label caps">Last name:</div><div class="hint">Eg: Dupont, Janssen, ...</div></div>
    <div class="abs sep" style="left:408px"></div>
    <div class="abs field" style="left:452px"><div class="label caps">Locality:</div><div class="hint">Eg: Brussels, Antwerp, 4000, ...</div></div>
    <div class="abs btn-search caps">Search</div>
  </form>

  <p class="abs browse caps">Or browse the highlights</p>
  <div class="abs cards caps">
    <div class="card">
      <svg viewBox="0 0 58 58" fill="none" stroke="#231b6e" stroke-width="2.2"><path d="M10 34a19 19 0 0 1 38 0z"/><path d="M6 38h46"/><circle cx="29" cy="12" r="3"/><path d="M12 42l-4 12M20 40l-6 14"/></svg>
      Food</div>
    <div class="card">
      <svg viewBox="0 0 58 58" fill="none" stroke="#231b6e" stroke-width="2.2"><rect x="5" y="16" width="48" height="34" rx="3"/><path d="M21 16V9h16v7M5 30h48"/><rect x="25" y="27" width="8" height="7"/></svg>
      Jobs</div>
    <div class="card">
      <svg viewBox="0 0 58 58" fill="none" stroke="#231b6e" stroke-width="2.2"><rect x="20" y="6" width="14" height="24" rx="7" transform="rotate(35 27 18)"/><circle cx="38" cy="28" r="7"/><path d="M4 40h12l10 4h10M4 52h34l16-12"/></svg>
      Medicals</div>
    <div class="card">
      <svg viewBox="0 0 58 58" fill="none" stroke="#231b6e" stroke-width="2.2"><path d="M8 18h42v36H8z"/><path d="M20 18v-6a9 9 0 0 1 18 0v6M22 28a7 7 0 0 0 14 0"/></svg>
      Shopping</div>
  </div>

  <aside class="abs ad ad-side">YOUR<br>AD<br>HERE</aside>
  <aside class="abs ad ad-wide" style="top:728px">YOUR AD HERE</aside>

  <h2 class="abs serif block-title" style="left:250px;top:903px">A Lorem Ipsum Dolor</h2>
  <div class="abs block-body" style="left:251px;top:973px;width:445px">
    <p>Lorem ipsum dolor sit amet, consectetur adipiscing elit. Nunc nisl nisi, tempus mollis eros ac, gravida consectetur dolor. Fusce sit amet scelerisque metus. In aliquam urna ac venenatis rhoncus.</p>
    <p>Pellentesque mattis maximus enim, ac euismod lectus vestibulum at. Aenean id tincidunt nibh, sed semper dui. Nulla eget ante et leo dictum venenatis. Integer nec purus aliquet.</p>
  </div>
  <div class="abs illus" role="img" aria-label="Illustration of a person beside a monitor with a large magnifying glass and chat bubbles" style="left:735px;top:885px;width:465px;height:282px;background:linear-gradient(135deg,#eef1fb 0%,#c9d3f4 55%,#f4c8cd 100%)"></div>

  <section class="abs app-band">
    <div class="abs phone-photo" role="img" aria-label="Photo of a hand holding a smartphone showing a starry galaxy screen"></div>
    <h2 class="abs serif app-title">Download our app</h2>
    <p class="abs app-body">Lorem ipsum dolor sit amet, consectetur adipiscing elit. Nunc nisl nisi, tempus mollis eros ac, gravida consectetur dolor. Fusce sit amet scelerisque metus. In aliquam urna ac venenatis rhoncus.</p>
    <div class="abs store-btn" style="left:767px">
      <svg width="36" height="40" viewBox="0 0 36 40" fill="none" stroke="#fff" stroke-width="2"><path d="M4 3l28 17L4 37z"/></svg>
      <div><div class="small">Get it on</div><div class="big">APP MARKET</div></div>
    </div>
    <div class="abs store-btn" style="left:1006px">
      <svg width="36" height="40" viewBox="0 0 36 40" fill="none" stroke="#fff" stroke-width="2"><rect x="5" y="6" width="26" height="30" rx="5"/><path d="M13 22h10"/></svg>
      <div><div class="small">Download on the</div><div class="big">APP SHELF</div></div>
    </div>
  </section>

  <aside class="abs ad ad-wide" style="top:1731px">YOUR AD HERE</aside>

  <div class="abs illus" role="img" aria-label="Illustration of two people with large Q and A letters, clouds and plants" style="left:228px;top:1905px;width:492px;height:270px;background:linear-gradient(135deg,#e6ecfb 0%,#aebff2 55%,#f7b7a8 100%)"></div>
  <h2 class="abs serif block-title" style="left:778px;top:1928px">A Lorem Ipsum Dolor</h2>
  <div class="abs block-body" style="left:778px;top:1999px;width:445px">
    <p>Lorem ipsum dolor sit amet, consectetur adipiscing elit. Nunc nisl nisi, tempus mollis eros ac, gravida consectetur dolor. Fusce sit amet scelerisque metus. In aliquam urna ac venenatis rhoncus.</p>
    <p>Pellentesque mattis maximus enim, ac euismod lectus vestibulum at. Aenean id tincidunt nibh, sed semper dui. Nulla eget ante et leo dictum venenatis. Integer nec purus aliquet.</p>
  </div>

  <footer class="abs site-footer">
    <div class="abs brand" style="left:199px;top:68px"><span class="brand-dot"></span><span class="brand-name">Dialbook</span></div>
    <p class="abs foot-about">Pellentesque mattis maximus enim, ac euismod lectus vestibulum at. Aenean id tincidunt nibh, sed semper dui.</p>
    <div class="abs" style="left:569px;top:42px">
      <h3 class="foot-head caps">Link</h3>
      <ul class="foot-list"><li>About Us</li><li>B2B Services</li><li>Help</li><li>General conditions of use</li><li>Data protection</li></ul>
    </div>
    <div class="abs" style="left:812px;top:42px">
      <h3 class="foot-head caps">About</h3>
      <div class="contact">
        <svg width="12" height="16" viewBox="0 0 12 16" fill="none" stroke="#fd5a5f" stroke-width="1.4"><path d="M6 15s5-5.5 5-9A5 5 0 0 0 1 6c0 3.5 5 9 5 9z"/><circle cx="6" cy="6" r="2"/></svg>
        <div>1234, Lorem ipsum<br>412 Rue des Tilleuls<br>1170 Brussels, Belgium</div>
      </div>
      <div class="contact" style="margin-top:6px">
        <svg width="14" height="12" viewBox="0 0 14 12" fill="none" stroke="#fd5a5f" stroke-width="1.4"><rect x="1" y="2" width="12" height="9"/><path d="M1 2l6 5 6-5"/></svg>
        <div>info@le5858.be</div>
      </div>
    </div>
    <div class="abs" style="left:1119px;top:42px">
      <h3 class="foot-head caps">Follow us</h3>
      <div class="social"><span></span><span></span><span></span></div>
    </div>
    <div class="abs foot-rule"></div>
    <p class="abs copyright caps">Copyright 2022 <b>Dialbook</b>. All rights reserved</p>
  </footer>

</div>
</body>
</html>
```